Business Card for Amber Heron Advisors

Business card design for Amber Heron Advisors, a new consulting and financial advisory firm. I would like the designs to integrate the logo attached (at least on 1 side).

Target Market(s)

individual and institutional clients

Contact Information for Business Card

Dominic L. Hartwell, CFA
Managing Director
amberheronadvisors.examplep
hartwell@amberheronadvisors.example
(555) 218-4903

```html
<!DOCTYPE html>
<html lang="en">
<head>
<meta charset="utf-8">
<title>Amber Heron Advisors – Business Card</title>
<link rel="stylesheet" href="https://fonts.googleapis.com/css2?family=Arimo:wght@400;700&display=swap">
<style>
  :root {
    --stage: #2a2a2a;
    --card-dark: #262626;
    --card-light: #ffffff;
    --amber: #d5781e;
    --ink: #222222;
    --ink-soft: #333333;
    --hairline: #d9d9d9;
  }
  * { box-sizing: border-box; margin: 0; padding: 0; }
  html, body { width: 1200px; height: 997px; overflow: hidden; }
  body {
    background: var(--stage);
    font-family: "Arimo", Arial, sans-serif;
    position: relative;
  }
  .card { position: absolute; box-shadow: 0 18px 40px rgba(0,0,0,.45); }

  /* Back side */
  .card-back {
    left: 90px; top: 330px; width: 560px; height: 320px;
    background: var(--card-dark);
    display: flex; align-items: center; justify-content: center;
  }
  .wordmark {
    display: flex; align-items: center; gap: 12px;
    color: var(--amber); font-weight: 400; letter-spacing: 2px;
    text-transform: uppercase; white-space: nowrap;
  }
  .wordmark-mark { width: 14px; height: 14px; background: var(--amber); }
  .card-back .wordmark { font-size: 30px; }

  /* Front side */
  .card-front {
    left: 760px; top: 220px; width: 330px; height: 577px;
    background: var(--card-light);
    display: flex; flex-direction: column;
  }
  .front-logo {
    height: 170px; display: flex; align-items: center; justify-content: center;
  }
  .front-logo .wordmark { font-size: 18px; gap: 8px; letter-spacing: 1px; }
  .front-logo .wordmark-mark { width: 10px; height: 10px; }
  .name-band {
    background: var(--amber); height: 68px;
    display: flex; flex-direction: column; align-items: center; justify-content: center;
  }
  .person-name { color: var(--ink); font-weight: 700; font-size: 15px; text-transform: uppercase; letter-spacing: .3px; }
  .person-title { color: var(--card-light); font-size: 12px; margin-top: 3px; }
  .contact-icons {
    display: flex; justify-content: center; gap: 16px; margin-top: 52px;
  }
  .contact-icons svg { width: 16px; height: 16px; fill: var(--amber); }
  .contact-list {
    list-style: none; text-align: center; margin-top: 38px;
    color: var(--ink-soft);
  }
  .contact-phone { font-size: 19px; }
  .contact-email { font-size: 15.5px; margin-top: 30px; }
  .contact-web { font-size: 16px; font-weight: 700; color: var(--amber); margin-top: 16px; }
  .footer-band { margin-top: auto; height: 62px; background: var(--amber); }
</style>
</head>
<body>
  <section class="card card-back" aria-label="Business card back">
    <div class="wordmark"><span class="wordmark-mark"></span>Amber Heron Advisors</div>
  </section>

  <section class="card card-front" aria-label="Business card front">
    <header class="front-logo">
      <div class="wordmark"><span class="wordmark-mark"></span>Amber Heron Advisors</div>
    </header>
    <div class="name-band">
      <p class="person-name">Dominic L. Hartwell, CFA</p>
      <p class="person-title">Managing Director</p>
    </div>
    <div class="contact-icons" aria-hidden="true">
      <svg viewBox="0 0 16 16"><path d="M2 6c0-2 2-3 6-3s6 1 6 3v1h-3V5.5H5V7H2z M4 8h8l1 6H3z"/><circle cx="8" cy="11" r="1.6" fill="#fff"/></svg>
      <svg viewBox="0 0 16 16"><rect x="1" y="3" width="14" height="10"/><path d="M1 3l7 6 7-6" fill="none" stroke="#fff" stroke-width="1.3"/></svg>
      <svg viewBox="0 0 16 16"><circle cx="8" cy="8" r="7"/><path d="M1 8h14M8 1c-3 3-3 11 0 14M8 1c3 3 3 11 0 14" fill="none" stroke="#fff" stroke-width="1"/></svg>
    </div>
    <ul class="contact-list">
      <li class="contact-phone">(555) 218-4903</li>
      <li class="contact-email">hartwell@amberheronadvisors.example</li>
      <li class="contact-web">www.amberheronadvisors.example</li>
    </ul>
    <div class="footer-band"></div>
  </section>
</body>
</html>
```